Harbor Lodge Sign for the road

Design an 8'x8' vector sign for the Harbor Lodge. The sign can only use two solid colors plus white. Use red, white, and blue. The sign will hang on the outside of the new motel. Include the phone number and website. 512-903-4417 harborlodgehub.org
I have attached the original sign that this will replace and also an idea of the american flag in the background of the words.

Target Market(s)

This will be seen by people driving by the non profit.

Industry/Entity Type

Non Profit

Logo Text

Harbor Lodge

Font styles to use
Other font styles liked:
• Black Ops One (or similar)

Colors
0355a3
ec1f27

Requirements
Must have
• Colors should be patriotic to the United States. This will need to have font that can be seen while driving.
Nice to have
• Somehow incorporate the American Flag or something patriotic.
Should not have
• Should not have very thin font.

```html
<!DOCTYPE html>
<html lang="en">
<head>
<meta charset="UTF-8">
<title>Harbor Lodge Road Sign</title>
<link rel="stylesheet" href="https://fonts.googleapis.com/css2?family=Black+Ops+One&display=swap">
<style>
  :root {
    --flag-red: #b3121b;
    --sign-red: #ec1f27;
    --sign-blue: #0355a3;
    --flag-navy: #0b1a4a;
    --white: #ffffff;
  }
  html, body {
    margin: 0;
    padding: 0;
    width: 1200px;
    height: 1200px;
    overflow: hidden;
    background: var(--white);
  }
  .sign {
    position: relative;
    width: 1200px;
    height: 1200px;
  }
  .sign svg {
    position: absolute;
    inset: 0;
    display: block;
  }
  .motel-name,
  .motel-word {
    font-family: "Black Ops One", sans-serif;
    fill: var(--white);
  }
  .brand-name {
    font-family: "Black Ops One", sans-serif;
    fill: var(--sign-blue);
  }
  .phone-number,
  .web-address {
    font-family: "Black Ops One", sans-serif;
    fill: var(--white);
  }
</style>
</head>
<body>
<main class="sign">
  <svg width="1200" height="1200" viewBox="0 0 1200 1200">
    <defs>
      <linearGradient id="canton-tone" x1="0" y1="0" x2="1" y2="1">
        <stop offset="0" stop-color="#050b24"/>
        <stop offset="1" stop-color="#0b1a4a"/>
      </linearGradient>
    </defs>

    <g class="flag-backdrop" role="img" aria-label="Waving American flag behind the sign panel">
      <rect x="0" y="0" width="1200" height="1200" fill="var(--white)"/>
      <rect x="0" y="0" width="1200" height="70" fill="var(--flag-red)"/>
      <rect x="0" y="140" width="1200" height="70" fill="var(--flag-red)"/>
      <rect x="0" y="280" width="1200" height="70" fill="var(--flag-red)"/>
      <rect x="0" y="1075" width="1200" height="45" fill="var(--flag-red)"/>
      <rect x="0" y="1160" width="1200" height="40" fill="var(--flag-red)"/>
      <rect x="0" y="0" width="460" height="360" fill="url(#canton-tone)"/>
    </g>

    <path class="panel-edge" d="M0 362 Q600 -40 1200 372 L1200 1066 L0 1066 Z" fill="var(--white)"/>
    <path class="panel" d="M0 376 Q600 -22 1200 386 L1200 1058 L0 1058 Z" fill="var(--sign-red)"/>

    <text class="motel-name" x="113" y="443" font-size="200" textLength="975" lengthAdjust="spacingAndGlyphs">EAGLE'S REST</text>
    <text class="motel-word" x="148" y="608" font-size="170" textLength="882" lengthAdjust="spacingAndGlyphs">MOTEL</text>

    <circle cx="395" cy="700" r="18" fill="var(--sign-blue)"/>
    <text class="brand-name" x="428" y="722" font-size="62">Harbor Lodge</text>

    <g class="phone-icon" fill="none" stroke="var(--white)" stroke-width="6">
      <circle cx="146" cy="862" r="40"/>
      <path d="M130 838 q-10 26 8 46 q10 10 22 10 l6 -10 l-12 -8 l-6 6 q-12 -10 -10 -26 l8 -2 l-2 -14 z" fill="var(--white)" stroke-width="2"/>
    </g>
    <text class="phone-number" x="236" y="897" font-size="100" textLength="855" lengthAdjust="spacingAndGlyphs">512.903.4417</text>

    <text class="web-address" x="152" y="1010" font-size="110" textLength="885" lengthAdjust="spacingAndGlyphs">harborlodgehub.org</text>
  </svg>
</main>
</body>
</html>
```